Peter Lanford Studios Business Card

Looking for a clear, modern, elegant, sharp business card that conveys a professional yet edgy image to my business as a wedding, portrait, and travel photographer. Would like something that looks vintage yet modern. Need a new business card to grow my business. We are growing the business for Wedding and Event Photography as well as fine art Photography. (Mostly Landscapes)
Updates

I’m looking through designs now but I have a new logo that i want using please.

New logo uploaded please redesign using that

PLEASE ALL DESIGNERS LOOK IN BRIEF FOR NEW LOGO

Target Market(s)

Brides, Grooms, Families with Kids, People looking for Fine Art Photography Artwork

Industry/Entity Type

Photographer

Contact Information for Business Card

Unsure

Font styles to use
Serif

Colors

Designer to choose colors to be used in the design.

Requirements
Must have
• My Website:
• http://lanfordgallery.snapfolio.example
• Phone:
• 555-418-2061
• Email:
• petelanfordgallery@mailbox.example
Nice to have
• Would like a sort of shine on the printing finish.
• I like black I think it looks good on a business card.
• Can try working with my logo (png that I've attached)

```html
<!DOCTYPE html>
<html lang="en">
<head>
<meta charset="utf-8">
<title>Peter Lanford Studios – Business Card</title>
<link rel="stylesheet" href="https://fonts.googleapis.com/css2?family=Raleway:wght@300;400;700&display=swap">
<style>
  :root {
    --card-dark: #202020;
    --brand-blue: #2b86d6;
    --band-blue: #4a9be3;
    --deep-blue: #1460a8;
    --ink-light: #ffffff;
    --ink-soft: #d9d9d9;
    --stage-light: #e6e6e6;
    --stage-dark: #5a5a5a;
  }
  * { margin: 0; padding: 0; box-sizing: border-box; }
  html, body { width: 1004px; height: 1200px; overflow: hidden; }
  body {
    position: relative;
    font-family: "Raleway", Arial, sans-serif;
    background: radial-gradient(ellipse at 85% 10%, var(--stage-light) 0%, #b5b5b5 45%, var(--stage-dark) 100%);
  }
  .card {
    position: absolute;
    left: 51px;
    width: 893px;
    height: 510px;
    background: var(--card-dark);
    overflow: hidden;
    box-shadow: 14px 14px 22px rgba(0,0,0,0.45);
  }
  .card--front { top: 53px; }
  .card--back { top: 631px; height: 511px; }
  .card__shapes { position: absolute; inset: 0; width: 100%; height: 100%; }

  .brand-mark {
    position: absolute;
    text-align: center;
    color: var(--ink-light);
    font-weight: 300;
    transform: translateX(-50%);
  }
  .brand-mark__square {
    display: block;
    margin: 0 auto;
    border: 2px solid var(--ink-light);
  }
  .brand-mark__name { display: block; white-space: nowrap; line-height: 1; }
  .brand-mark__sub { display: block; white-space: nowrap; line-height: 1; }

  .card--front .brand-mark { left: 446px; top: 168px; }
  .card--front .brand-mark__square { width: 83px; height: 83px; margin-bottom: 33px; }
  .card--front .brand-mark__name { font-size: 38px; color: var(--ink-soft); }
  .card--front .brand-mark__sub { font-size: 17px; letter-spacing: 10px; margin-top: 12px; padding-left: 10px; color: var(--ink-soft); }

  .card--back .brand-mark { left: 726px; top: 189px; }
  .card--back .brand-mark__square { width: 64px; height: 64px; margin-bottom: 25px; }
  .card--back .brand-mark__name { font-size: 29px; }
  .card--back .brand-mark__sub { font-size: 14px; letter-spacing: 8px; margin-top: 9px; padding-left: 8px; }

  .person {
    position: absolute;
    left: 64px;
    top: 92px;
  }
  .person__name {
    font-size: 38px;
    font-weight: 700;
    color: var(--ink-light);
    line-height: 1;
    letter-spacing: 0.5px;
  }
  .person__role {
    font-size: 23px;
    font-weight: 300;
    color: var(--brand-blue);
    line-height: 1;
    margin-top: 8px;
  }
  .person__rule {
    position: absolute;
    left: 44px;
    top: 179px;
    width: 314px;
    height: 2px;
    background: linear-gradient(90deg, rgba(43,134,214,0) 0%, var(--brand-blue) 35%, var(--brand-blue) 70%, rgba(43,134,214,0) 100%);
  }

  .contact-list { position: absolute; left: 40px; top: 233px; list-style: none; }
  .contact-list__item {
    display: flex;
    align-items: center;
    height: 32px;
    margin-bottom: 20px;
    color: var(--ink-light);
    font-size: 18.5px;
    white-space: nowrap;
  }
  .contact-list__item:nth-child(4) { margin-top: 3px; }
  .contact-list__icon {
    width: 32px; height: 32px;
    border-radius: 50%;
    background: var(--band-blue);
    display: flex; align-items: center; justify-content: center;
    margin-right: 17px;
    flex: none;
  }
  .contact-list__icon svg { width: 18px; height: 18px; }
</style>
</head>
<body>

<section class="card card--front" aria-label="Card front">
  <svg class="card__shapes" viewBox="0 0 893 510" aria-hidden="true">
    <polygon points="0,142 286,142 253,174 0,174" fill="#1e63a8"/>
    <polygon points="0,137 279,137 250,166 0,166" fill="var(--band-blue)"/>
    <polygon points="642,367 893,367 893,398 611,398" fill="#1e63a8"/>
    <polygon points="651,373 893,373 893,404 619,404" fill="var(--band-blue)"/>
  </svg>
  <div class="brand-mark">
    <span class="brand-mark__square"></span>
    <span class="brand-mark__name">PETER LANFORD</span>
    <span class="brand-mark__sub">STUDIOS</span>
  </div>
</section>

<section class="card card--back" aria-label="Card back">
  <svg class="card__shapes" viewBox="0 0 893 511" aria-hidden="true">
    <defs>
      <filter id="panel-shadow" x="-20%" y="-20%" width="140%" height="140%">
        <feDropShadow dx="-6" dy="4" stdDeviation="6" flood-color="#000" flood-opacity="0.5"/>
      </filter>
    </defs>
    <polygon points="548,352 600,511 470,511" fill="var(--deep-blue)" filter="url(#panel-shadow)"/>
    <line x1="547" y1="356" x2="466" y2="511" stroke="#ffffff" stroke-width="5"/>
    <polygon points="694,0 893,0 893,511 597,511 487,164" fill="var(--brand-blue)" filter="url(#panel-shadow)"/>
  </svg>

  <div class="person">
    <h1 class="person__name">PETER LANFORD</h1>
    <p class="person__role">PHOTOGRAPHER</p>
  </div>
  <div class="person__rule"></div>

  <ul class="contact-list">
    <li class="contact-list__item">
      <span class="contact-list__icon">
        <svg viewBox="0 0 24 24"><path fill="#fff" d="M6.6 10.8a15.2 15.2 0 0 0 6.6 6.6l2.2-2.2a1 1 0 0 1 1-.25 11.4 11.4 0 0 0 3.6.57 1 1 0 0 1 1 1V20a1 1 0 0 1-1 1A17 17 0 0 1 3 4a1 1 0 0 1 1-1h3.5a1 1 0 0 1 1 1c0 1.25.2 2.45.57 3.57a1 1 0 0 1-.25 1z"/></svg>
      </span>555-418-2061
    </li>
    <li class="contact-list__item">
      <span class="contact-list__icon">
        <svg viewBox="0 0 24 24"><path fill="#fff" d="M3 6h18v12H3z"/><path fill="none" stroke="var(--band-blue)" stroke-width="1.6" d="M3 6l9 7 9-7M3 18l7-6M21 18l-7-6"/></svg>
      </span>petelanfordgallery@mailbox.example
    </li>
    <li class="contact-list__item">
      <span class="contact-list__icon">
        <svg viewBox="0 0 24 24"><path fill="#fff" d="M12 2a7 7 0 0 0-7 7c0 5 7 13 7 13s7-8 7-13a7 7 0 0 0-7-7zm0 9.5A2.5 2.5 0 1 1 12 6.5a2.5 2.5 0 0 1 0 5z"/></svg>
      </span>Address, Street, City
    </li>
    <li class="contact-list__item">
      <span class="contact-list__icon">
        <svg viewBox="0 0 24 24"><g fill="none" stroke="#fff" stroke-width="1.6"><circle cx="12" cy="12" r="9"/><ellipse cx="12" cy="12" rx="4" ry="9"/><path d="M3 12h18M4.5 7.5h15M4.5 16.5h15"/></g></svg>
      </span>http://lanfordgallery.snapfolio.example
    </li>
  </ul>

  <div class="brand-mark">
    <span class="brand-mark__square"></span>
    <span class="brand-mark__name">PETER LANFORD</span>
    <span class="brand-mark__sub">STUDIOS</span>
  </div>
</section>

</body>
</html>
```